Criação de Cartao de Visita para Computador & Internet
" Nossos clientes fazem o outsorcing da TI para nós, assim cuidamos de todos os recursos se serviços de TI, também vendemos hardwares e softwares "

```html
<!DOCTYPE html>
<html lang="pt-BR">
<head>
<meta charset="utf-8">
<title>NVT Corp — Cartão de Visita</title>
<link href="https://fonts.googleapis.com/css2?family=Roboto:wght@400;500;700;900&display=swap" rel="stylesheet">
<style>
  :root{
    --bg:#e6e8ea;
    --white:#ffffff;
    --blue-dark:#0d5f97;
    --blue:#1b84c6;
    --blue-light:#4fb3e6;
    --ink:#1f3344;
    --grey:#6d7b86;
  }
  *{box-sizing:border-box;margin:0;padding:0}
  html,body{width:1200px;height:1200px;overflow:hidden}
  body{background:var(--bg);font-family:"Roboto",Arial,sans-serif;position:relative}
  .card{position:absolute;left:160px;width:880px;height:503px;border-radius:6px;overflow:hidden;box-shadow:0 10px 30px rgba(0,0,0,.15)}
  .card--front{top:68px;background:var(--white)}
  .card--back{top:630px;background:linear-gradient(135deg,var(--blue-light) 0%,var(--blue) 45%,var(--blue-dark) 100%)}

  /* front */
  .front-band{position:absolute;left:0;right:0;bottom:0;height:34px;background:linear-gradient(90deg,var(--blue-light),var(--blue-dark))}
  .brand{position:absolute;left:70px;top:175px;display:flex;align-items:center;gap:22px}
  .brand__mark{width:110px;height:110px;border-radius:50%;background:var(--blue)}
  .brand__name{font-size:52px;font-weight:700;color:var(--blue)}
  .person{position:absolute;left:470px;top:90px}
  .person__head{display:flex;align-items:center;gap:14px}
  .person__icon{width:46px;height:46px;background:var(--blue-dark);border-radius:4px;display:flex;align-items:center;justify-content:center}
  .person__name{font-size:34px;font-weight:500;color:var(--ink);line-height:1}
  .person__role{font-size:14px;color:var(--grey);margin-top:4px}
  .person__division{margin-top:22px;font-size:24px;font-weight:900;color:var(--blue)}
  .contacts{list-style:none;margin-top:18px}
  .contacts li{display:flex;align-items:center;gap:12px;font-size:17px;color:var(--ink);margin-bottom:9px}
  .contacts .ico{width:24px;height:24px;background:var(--blue-dark);border-radius:3px;display:flex;align-items:center;justify-content:center;flex:none}

  /* back */
  .divisions{position:absolute;inset:0;display:flex;padding:70px 60px}
  .division{flex:1;color:var(--white);padding:0 30px}
  .division + .division{border-left:2px solid rgba(255,255,255,.6)}
  .division__title{font-size:30px;font-weight:900;letter-spacing:.5px}
  .division__sub{font-size:14px;opacity:.85;margin:4px 0 22px}
  .division__list{list-style:none}
  .division__list li{position:relative;padding-left:24px;font-size:18px;font-weight:500;margin-bottom:11px;line-height:1.2}
  .division__list li::before{content:"";position:absolute;left:2px;top:6px;width:9px;height:9px;border-radius:50%;background:var(--white)}
</style>
</head>
<body>

<section class="card card--front">
  <div class="brand">
    <div class="brand__mark"></div>
    <div class="brand__name">NVT Corp</div>
  </div>

  <div class="person">
    <div class="person__head">
      <div class="person__icon">
        <svg width="26" height="26" viewBox="0 0 24 24"><circle cx="12" cy="8" r="5" fill="#fff"/><path d="M3 23c0-5 4-8 9-8s9 3 9 8z" fill="#fff"/></svg>
      </div>
      <div>
        <div class="person__name">Marina Toledo</div>
        <div class="person__role">Gerente de Eventos</div>
      </div>
    </div>
    <div class="person__division">DIVISÃO DE EVENTOS</div>
    <ul class="contacts">
      <li><span class="ico"><svg width="14" height="14" viewBox="0 0 24 24"><path d="M6 2l4 5-2 3c1 3 3 5 6 6l3-2 5 4-3 4C10 22 2 14 2 5z" fill="#fff"/></svg></span>11 3400 - 1200 (SP)</li>
      <li><span class="ico"><svg width="14" height="14" viewBox="0 0 24 24"><path d="M6 2l4 5-2 3c1 3 3 5 6 6l3-2 5 4-3 4C10 22 2 14 2 5z" fill="#fff"/></svg></span>0800 700 1234 (Demais Localidades)</li>
      <li><span class="ico"><svg width="14" height="14" viewBox="0 0 24 24"><rect x="6" y="1" width="12" height="22" rx="2" fill="#fff"/><rect x="8" y="4" width="8" height="14" fill="#0d5f97"/></svg></span>11 99000 - 4321</li>
      <li><span class="ico"><svg width="14" height="14" viewBox="0 0 24 24"><rect x="1" y="4" width="22" height="16" rx="1" fill="#fff"/><path d="M1 5l11 8 11-8" stroke="#0d5f97" stroke-width="2" fill="none"/></svg></span>contato@nvtcorp.com.br</li>
    </ul>
  </div>

  <div class="front-band"></div>
</section>

<section class="card card--back">
  <div class="divisions">
    <div class="division">
      <h2 class="division__title">DIVISÃO DE TI</h2>
      <p class="division__sub">Soluções em Tecnologia da Informação</p>
      <ul class="division__list">
        <li>Administração e Suporte de TI / Outsourcing</li>
        <li>Cloud Solutions</li>
        <li>Consultoria e Venda de Hardware e Software</li>
        <li>Segurança e Proteção de Dados</li>
      </ul>
    </div>
    <div class="division">
      <h2 class="division__title">DIVISÃO DE EVENTOS</h2>
      <p class="division__sub">Eventos corporativos sob medida</p>
      <ul class="division__list">
        <li>Congressos</li>
        <li>Treinamentos</li>
        <li>Convenções</li>
        <li>Feiras</li>
        <li>Workshop</li>
        <li>Networking</li>
        <li>Eventos Empresariais</li>
      </ul>
    </div>
  </div>
</section>

</body>
</html>
```